Flyer für Immobilienmakler
Top Arbeit vom Designer. Er hat alle Idee schnell und professionell umgesetzt und das Ergebnis kann sich sehen lassen. Herzlichen Dank für die großartige Arbeit. Immer wieder gerne.
Zielgruppe
Immobilienmakler, Zielgruppe sind Menschen die uns weiterempfehlen um ihre Immobilie zu verkaufen
Aufgabenstellung
Ein Flyer DIN lang quer, Vorder und Rückseite, Es geht um eine Tippgeberprovision welche Menschen bekommen die uns einen Verkaufskunden bringen, diese erhalten 10 %- genaue Texte und Hinweise werde ich einbringen, Unser Slogan: 'Unsere Erfahrung für Ihren Vorteil'
Nachtrag. Bei dem Flyer 'Vom Berg Immobilien' finde ich die blauen Banner/ Streifen gut- ist aber kein Muss. Update: Es war als Inspiration von meiner Seite gedacht. Auf keinen Fall darf es genauso aussehen!!
Meine jetzige Webseite ist auch gut um die Farben zu erkennen, jedoch nicht unbedingt das Design, da ich gerade eine neue Webseite erstellen lasse

```html
<!DOCTYPE html>
<html lang="de">
<head>
<meta charset="utf-8">
<title>Lorant Immobilien – Flyer DIN lang</title>
<link rel="stylesheet" href="https://fonts.googleapis.com/css2?family=Montserrat:wght@400;500;600;700&display=swap">
<style>
  :root {
    --navy: #2d3461;
    --ink: #2b3160;
    --page: #f6f6f6;
    --paper: #ffffff;
    --ghost: #e8e7f0;
    --ghost-soft: #efeff2;
  }
  * { margin: 0; padding: 0; box-sizing: border-box; }
  html, body { width: 1200px; height: 1200px; overflow: hidden; }
  body {
    background: var(--page);
    font-family: "Montserrat", Arial, sans-serif;
    color: var(--ink);
    position: relative;
  }
  .flyer {
    position: absolute;
    left: 40px;
    top: 320px;
    width: 1120px;
    height: 560px;
    background: var(--paper);
    overflow: hidden;
  }
  .ghost-mark {
    position: absolute;
    left: 226px;
    top: 150px;
    font-size: 118px;
    font-weight: 700;
    letter-spacing: 4px;
    color: var(--ghost);
    line-height: 1;
  }
  .ghost-sub {
    position: absolute;
    left: 656px;
    top: 318px;
    font-size: 42px;
    font-weight: 400;
    color: var(--ghost-soft);
    line-height: 1;
  }
  .services {
    position: absolute;
    left: 30px;
    top: 50px;
    list-style: none;
  }
  .services li {
    display: flex;
    align-items: center;
    font-size: 23px;
    font-weight: 600;
    letter-spacing: 0.8px;
    line-height: 1;
    height: 28px;
  }
  .services li + li { margin-top: 14px; }
  .services li:last-child { margin-top: 18px; }
  .services svg { width: 18px; height: 18px; margin-right: 7px; flex: none; }
  .intro {
    position: absolute;
    left: 55px;
    top: 228px;
    font-size: 19px;
    font-weight: 400;
    line-height: 30px;
    letter-spacing: 0.2px;
  }
  .intro strong { font-weight: 700; }
  .signature {
    position: absolute;
    left: 35px;
    top: 306px;
    width: 252px;
    height: 60px;
    background: linear-gradient(90deg, #eef0fa, #f6f7fc);
  }
  .signer {
    position: absolute;
    left: 55px;
    top: 368px;
    font-size: 14px;
    font-weight: 500;
  }
  .portrait { position: absolute; left: 0; top: 0; }
  .rule {
    position: absolute;
    left: 0;
    width: 1120px;
    height: 2px;
    background: var(--navy);
  }
  .rule--top { top: 443px; }
  .rule--bottom { top: 529px; }
  .band {
    position: absolute;
    top: 450px;
    height: 74px;
    background: var(--navy);
  }
  .band--main { left: 0; width: 848px; }
  .band--end { left: 1080px; width: 40px; }
  .brand {
    position: absolute;
    left: 848px;
    top: 450px;
    width: 232px;
    height: 74px;
    display: flex;
    align-items: center;
    justify-content: center;
    font-size: 36px;
    font-weight: 600;
    letter-spacing: 3px;
    color: var(--navy);
  }
</style>
</head>
<body>
  <section class="flyer">
    <div class="ghost-mark" aria-hidden="true">LORANT</div>
    <div class="ghost-sub" aria-hidden="true">Immobilien</div>

    <ul class="services">
      <li><svg viewBox="0 0 18 18"><path d="M3 9l4 4 8-8" fill="none" stroke="#2b3160" stroke-width="2.6" stroke-linecap="round" stroke-linejoin="round"/></svg>WERTERMITTLUNGEN</li>
      <li><svg viewBox="0 0 18 18"><path d="M3 9l4 4 8-8" fill="none" stroke="#2b3160" stroke-width="2.6" stroke-linecap="round" stroke-linejoin="round"/></svg>GUTACHTEN</li>
      <li><svg viewBox="0 0 18 18"><path d="M3 9l4 4 8-8" fill="none" stroke="#2b3160" stroke-width="2.6" stroke-linecap="round" stroke-linejoin="round"/></svg>KAUF- UND VERKAUFSBERATUNG</li>
      <li><svg viewBox="0 0 18 18"><path d="M3 9l4 4 8-8" fill="none" stroke="#2b3160" stroke-width="2.6" stroke-linecap="round" stroke-linejoin="round"/></svg>ENERGIEAUSWEIS</li>
    </ul>

    <p class="intro">oder Fragen zu Immobilien bei Erbschaft oder Scheidung.<br><strong>Wir beraten Sie!</strong> Objektiv, erfahren und zertifiziert.</p>

    <div class="signature" role="img" aria-label="Handschriftliche Unterschrift von Hans Lindenhuber"></div>
    <p class="signer">Hans Lindenhuber</p>

    <svg class="portrait" width="1120" height="380" viewBox="0 0 1120 380">
      <defs>
        <linearGradient id="portraitTone" x1="0" y1="0" x2="1" y2="1">
          <stop offset="0" stop-color="#6b4a2c"/>
          <stop offset="0.5" stop-color="#7d6a5c"/>
          <stop offset="1" stop-color="#3a4560"/>
        </linearGradient>
        <filter id="frameShadow" x="-10%" y="-10%" width="130%" height="130%">
          <feDropShadow dx="-3" dy="4" stdDeviation="4" flood-color="#000" flood-opacity="0.22"/>
        </filter>
      </defs>
      <polygon points="824,0 1120,0 1120,361 774,302" fill="#ffffff" filter="url(#frameShadow)"/>
      <polygon points="840,0 1120,0 1120,345 789,291" fill="url(#portraitTone)" role="img" aria-label="Porträtfoto des Immobilienberaters im Anzug"/>
    </svg>

    <div class="rule rule--top"></div>
    <div class="band band--main"></div>
    <div class="brand">LORANT</div>
    <div class="band band--end"></div>
    <div class="rule rule--bottom"></div>
  </section>
</body>
</html>
```